Design for Agenda app (online tool) (#102244)

Url of the app: http://notes.bluefernlab.dk

It currently has 3 main parts:
- Front: http://fernhost.dk/screencast/2015-12-01_12-53-36.png
- Dashboard: http://fernhost.dk/screencast/2015-12-01_12-54-16.png
- Meeting page: http://fernhost.dk/screencast/2015-12-01_12-54-53.png

The idea of the app is to have virtual meetings with other people, to take notes/minutes online and to share what is written.

Unregistered users can see only the front.

Registered users can see front, their own dashboard and the meetings which they created or to which they were invited.

The meeting itself has two roles - minute taker an attendee. The attendee can edit only the agenda so he should have different view for the other parts of the meeting compared to the minute taker who can edit everything.

In this doc it is described what are the elements per page which we want to have
https://files.example-docs.net/d/7qXk2LmPz9RtYv4NcBw8HsJd3FgA6eUo1KtQ5WnZ0yE/edit?usp=sharing

As you can see, there is some inconsistency between the front page and the rest of the app. We would like to make it look professional and consistent on all places.

Goal: Get new responsive design where all main parts(front page, dashboard page, meeting page and profile page) will be consistent with each other.

The design should be clean, simple and with very friendly UX.
Updates

Industry/Entity Type

Online

Number of Pages Required

3 page

Font styles to use
Sans Serif

Requirements
Must have
• - Clean and simple
• - Very friendly UX

```html
<!DOCTYPE html>
<html lang="en">
<head>
<meta charset="utf-8">
<title>Fernline Agenda – Meeting</title>
<link href="https://fonts.googleapis.com/css2?family=Roboto:wght@400;500&display=swap" rel="stylesheet">
<style>
:root{
  --navy:#1c3347;
  --teal:#2ec4cc;
  --teal-line:#4fb7b3;
  --btn:#5fbfb8;
  --btn-edge:#4aa7a0;
  --page:#e9e8e1;
  --white:#ffffff;
  --ink:#333333;
  --muted:#8a8a8a;
  --rule:#d9d9d4;
  --head:#d6d5c8;
  --plus:#8cc63f;
  --help:#3fb6b8;
  --orange:#f39a1e;
  --green:#6aaa1e;
  --blue:#1e7fbf;
  --cross:#666666;
}
*{box-sizing:border-box;margin:0;padding:0}
html,body{width:1200px;height:895px;overflow:hidden}
body{font-family:"Roboto",sans-serif;background:var(--page);color:var(--ink);position:relative}
.topbar{position:absolute;left:0;top:0;width:1200px;height:65px;background:var(--navy);border-bottom:4px solid var(--teal-line)}
.brand{position:absolute;left:15px;top:11px;display:flex;align-items:center;gap:14px;color:var(--white);font-size:24px;font-weight:400}
.brand-dot{width:40px;height:40px;border-radius:50%;background:var(--teal)}
.nav-cell{position:absolute;top:0;height:65px;width:71px;border-left:1px solid #34495c;display:flex;align-items:center;justify-content:center}
.nav-add{left:849px}
.nav-help{left:920px;border-right:1px solid #34495c}
.user{position:absolute;left:991px;top:2px;width:209px;height:61px;background:var(--teal);display:flex;align-items:center;padding-left:11px;color:var(--white);font-size:14.5px;font-weight:500;gap:9px}
.avatar{width:34px;height:34px;border-radius:50%;background:var(--white);display:flex;align-items:flex-end;justify-content:center;overflow:hidden}
.title-band{position:absolute;left:0;top:69px;width:1200px;height:76px;background:var(--white);border-bottom:1px solid var(--rule)}
.title-band h1{position:absolute;left:75px;top:27px;font-size:19px;font-weight:400;color:#444}
.meta{position:absolute;left:74px;top:166px;height:37px;display:flex;align-items:center;font-size:13.5px;color:#555}
.meta .item{display:flex;align-items:center;gap:5px}
.caret{width:0;height:0;border-left:4px solid transparent;border-right:4px solid transparent;border-top:5px solid #555;margin-left:4px}
.tz{position:absolute;left:324px;top:166px;width:131px;height:37px;background:var(--white);border:1px solid var(--rule);border-radius:3px;display:flex;align-items:center;padding-left:13px;font-size:15px;color:#444;gap:12px}
.pin{position:absolute;left:472px;top:176px}
.place{position:absolute;left:491px;top:166px;width:87px;height:37px;background:var(--white);border-radius:3px;display:flex;align-items:center;padding-left:11px;font-size:15px;color:#555}
.label{position:absolute;left:74px;font-size:14.5px;font-weight:500;color:#333}
.field{position:absolute;left:72px;width:1052px;height:38px;background:var(--white);border:1px solid var(--rule);border-radius:3px;display:flex;align-items:center;padding-left:11px;font-size:14.5px;color:#777}
.chips{padding-left:2px;gap:3px}
.chip{background:#e5e5df;height:33px;display:flex;align-items:center;padding:0 10px 0 8px;font-size:14.5px;color:#333;gap:9px}
.chip b{font-size:13px}
.hint{margin-left:10px;font-size:14px;color:#999}
.agenda{position:absolute;left:74px;top:427px;width:1052px;background:var(--white);border-top:3px solid var(--head);border-bottom:1px solid var(--rule)}
.agenda-row{height:46px;display:flex;align-items:center;padding-left:15px;font-size:14.5px;position:relative}
.agenda-row+.agenda-row{border-top:1px solid var(--rule)}
.agenda-row .num{width:33px}
.placeholder{color:#999}
.cross{position:absolute;right:16px;top:50%;margin-top:-7px}
.minutes{position:absolute;left:74px;top:574px;width:1052px;background:var(--white);border-collapse:collapse;font-size:14.5px}
.minutes th{background:var(--head);height:41px;text-align:left;font-weight:500;font-size:14.5px;color:#333}
.minutes td{height:46px;border-bottom:1px solid var(--rule);position:relative}
.minutes tr.group td{height:31px;padding-left:10px}
.type{display:flex;align-items:center;padding-left:47px;width:221px}
.type .no{width:30px;color:#555}
.type .tag{flex:1}
.q{color:var(--orange)}.i{color:var(--green)}.t{color:var(--blue)}
.actions{position:absolute;top:816px;left:0;width:1200px;display:flex;justify-content:center;gap:9px}
.btn{height:48px;background:var(--btn);border:1px solid var(--btn-edge);display:flex;align-items:center;color:var(--white);font-size:17px;font-weight:500}
.btn .ico{width:45px;height:100%;border-right:1px solid var(--btn-edge);display:flex;align-items:center;justify-content:center}
.btn span{padding:0 16px 0 13px}
</style>
</head>
<body>
<header class="topbar">
  <div class="brand"><div class="brand-dot"></div>Fernline Agenda</div>
  <div class="nav-cell nav-add">
    <svg width="38" height="38" viewBox="0 0 38 38"><circle cx="19" cy="19" r="17" fill="none" stroke="var(--plus)" stroke-width="3"/><path d="M19 11v16M11 19h16" stroke="var(--plus)" stroke-width="4"/></svg>
  </div>
  <div class="nav-cell nav-help">
    <svg width="38" height="38" viewBox="0 0 38 38"><circle cx="19" cy="19" r="17" fill="none" stroke="var(--help)" stroke-width="3"/><text x="19" y="26" text-anchor="middle" font-family="Roboto,sans-serif" font-weight="500" font-size="20" fill="var(--help)">?</text></svg>
  </div>
  <div class="user">
    <div class="avatar"><svg width="24" height="28" viewBox="0 0 24 28"><circle cx="12" cy="9" r="6" fill="#b9b9b9"/><path d="M0 28c0-8 5-11 12-11s12 3 12 11z" fill="#b9b9b9"/></svg></div>
    Milen Petrov
    <svg width="12" height="8" viewBox="0 0 12 8" style="margin-left:6px"><path d="M0 0h12L6 8z" fill="#fff"/></svg>
  </div>
</header>

<section class="title-band"><h1>Demo title</h1></section>

<div class="meta">
  <div class="item"><svg width="13" height="13" viewBox="0 0 13 13"><rect x="1" y="2" width="11" height="10" fill="none" stroke="var(--help)" stroke-width="1.2"/><path d="M1 5h11M4 0v3M9 0v3" stroke="var(--help)" stroke-width="1.2"/></svg>11,12,2015<i class="caret"></i></div>
  <div class="item" style="margin-left:19px"><svg width="14" height="14" viewBox="0 0 14 14"><circle cx="7" cy="7" r="6" fill="none" stroke="var(--help)" stroke-width="1.3"/><path d="M7 3.5V7h3" fill="none" stroke="var(--help)" stroke-width="1.3"/></svg>13:08<i class="caret"></i></div>
  <div class="item" style="margin-left:8px">-&nbsp;&nbsp;15:08<i class="caret"></i></div>
</div>
<div class="tz">(GMT+01:00)<i class="caret"></i></div>
<svg class="pin" width="10" height="14" viewBox="0 0 10 14"><path d="M5 13S1 8 1 5a4 4 0 0 1 8 0c0 3-4 8-4 8z" fill="none" stroke="var(--help)" stroke-width="1.2"/><circle cx="5" cy="5" r="1.5" fill="var(--help)"/></svg>
<div class="place">@callroom</div>

<div class="label" style="top:220px">Minute taker</div>
<div class="field" style="top:247px">Daria Koleva</div>

<div class="label" style="top:311px">Atendees</div>
<div class="field chips" style="top:339px">
  <div class="chip">Daria Kolewa <b>x</b></div>
  <div class="chip">Milen Petrov <b>x</b></div>
  <div class="hint">Type e-mail to add new attendee. At the end, press enter, space or type comma to insent it.</div>
</div>

<div class="label" style="top:402px">About this meeting/Agenda</div>
<div class="agenda">
  <div class="agenda-row"><span class="num">1.</span>Test agenda item #1
    <svg class="cross" width="14" height="14" viewBox="0 0 14 14"><path d="M1 1l12 12M13 1L1 13" stroke="var(--cross)" stroke-width="2.6"/></svg></div>
  <div class="agenda-row placeholder"><span class="num">2.</span>Type here to add a new item to the agenda</div>
</div>

<div class="label" style="top:548px">Meeting minutes</div>
<table class="minutes">
  <tr><th style="width:230px;padding-left:9px">Type</th><th style="width:630px">Note</th><th>Owner</th></tr>
  <tr class="group"><td colspan="3">1. Test agenda item #1</td></tr>
  <tr><td><div class="type"><span class="no">1.0</span><span class="tag q">Question</span><i class="caret"></i></div></td><td>Test note #1</td><td>Milen Petrov<svg class="cross" width="14" height="14" viewBox="0 0 14 14"><path d="M1 1l12 12M13 1L1 13" stroke="var(--cross)" stroke-width="2.6"/></svg></td></tr>
  <tr><td><div class="type"><span class="no">1.1</span><span class="tag i">idea</span><i class="caret"></i></div></td><td>Test note #2</td><td>Daria Koleva<svg class="cross" width="14" height="14" viewBox="0 0 14 14"><path d="M1 1l12 12M13 1L1 13" stroke="var(--cross)" stroke-width="2.6"/></svg></td></tr>
  <tr><td><div class="type"><span class="no">1.0</span><span class="tag t">To Do</span><i class="caret"></i></div></td><td class="placeholder">Type here to add new note to agenda item #1</td><td class="placeholder">Owner</td></tr>
</table>

<div class="actions">
  <div class="btn"><div class="ico"><svg width="26" height="20" viewBox="0 0 26 20"><rect width="26" height="20" rx="2" fill="#fff"/><path d="M1 2l12 9 12-9" fill="none" stroke="var(--btn)" stroke-width="2"/></svg></div><span>Send Invites</span></div>
  <div class="btn"><div class="ico"><svg width="30" height="30" viewBox="0 0 30 30"><circle cx="15" cy="15" r="13" fill="none" stroke="#fff" stroke-width="2.2"/><path d="M15 8v8h6" fill="none" stroke="#fff" stroke-width="2.2"/><text x="3" y="11" font-family="Roboto,sans-serif" font-size="9" font-weight="500" fill="#fff">15</text></svg></div><span>Send minutes as email</span></div>
  <div class="btn"><div class="ico"><svg width="30" height="28" viewBox="0 0 30 28"><rect x="8" y="1" width="14" height="8" fill="#fff"/><rect x="1" y="9" width="28" height="12" rx="2" fill="#fff"/><rect x="7" y="16" width="16" height="11" fill="#fff" stroke="var(--btn)" stroke-width="1.5"/></svg></div><span>Print</span></div>
  <div class="btn"><div class="ico"><svg width="20" height="26" viewBox="0 0 20 26"><rect x="0" y="3" width="20" height="3" fill="#fff"/><rect x="7" y="0" width="6" height="3" fill="#fff"/><path d="M2 8h16v18H2z" fill="#fff"/><path d="M6 11v12M10 11v12M14 11v12" stroke="var(--btn)" stroke-width="1.6"/></svg></div><span>Delete</span></div>
</div>
</body>
</html>
```